Business Card

We need some ideas for corporate business cards. I'm interested in a double sided card, with one side featuring our corporate logo, the other side with employee information.

Corporate colors, logo etc. available at www.brivalo.com

Industry/Entity Type

Business

Requirements
Must have
• The "Brivalo" logo with stylized "O"

Nice to have
• Preferred font is calibri

```html
<!DOCTYPE html>
<html lang="en">
<head>
<meta charset="utf-8">
<title>Brivalo Business Card</title>
<link href="https://fonts.googleapis.com/css2?family=Carlito:wght@400;700&display=swap" rel="stylesheet">
<style>
  :root {
    --backdrop: #e2dedf;
    --brand-orange: #f28c12;
    --brand-orange-light: #f59a2a;
    --brand-blue: #4f9fd8;
    --ink: #111111;
    --paper: #ffffff;
  }
  html, body {
    margin: 0;
    padding: 0;
    width: 1200px;
    height: 1000px;
    overflow: hidden;
    background: var(--backdrop);
    font-family: "Carlito", Calibri, sans-serif;
  }
  .canvas {
    position: relative;
    width: 1200px;
    height: 1000px;
  }
  .card {
    position: absolute;
    overflow: hidden;
  }
  .orange-surface {
    background: radial-gradient(circle at 40% 40%, var(--brand-orange-light), var(--brand-orange) 75%);
  }
  /* Front side */
  .card-front {
    left: 16px;
    top: 13px;
    width: 765px;
    height: 466px;
  }
  .front-wordmark {
    position: absolute;
    left: 34px;
    top: 178px;
    height: 104px;
    display: flex;
    align-items: center;
    gap: 30px;
  }
  .front-wordmark .mark-square {
    width: 104px;
    height: 104px;
    background: var(--brand-blue);
  }
  .front-wordmark .brand-name {
    color: var(--paper);
    font-weight: 400;
    font-size: 160px;
    line-height: 1;
    letter-spacing: 4px;
    margin-top: 6px;
  }
  /* Back side */
  .card-back {
    left: 411px;
    top: 513px;
    width: 765px;
    height: 467px;
    display: flex;
  }
  .back-color-panel {
    width: 500px;
    height: 100%;
  }
  .back-info-panel {
    position: relative;
    width: 265px;
    height: 100%;
    background: var(--paper);
    color: var(--ink);
    text-align: center;
  }
  .back-wordmark {
    position: absolute;
    left: 13px;
    top: 14px;
    display: flex;
    align-items: center;
    gap: 10px;
  }
  .back-wordmark .mark-square {
    width: 31px;
    height: 31px;
    background: var(--brand-blue);
  }
  .back-wordmark .brand-name {
    font-weight: 400;
    font-size: 50px;
    line-height: 1;
    letter-spacing: 1px;
    margin-top: 3px;
  }
  .employee-name {
    position: absolute;
    left: 0; right: 0;
    top: 173px;
    font-size: 22px;
  }
  .employee-phone {
    position: absolute;
    left: 0; right: 0;
    top: 208px;
    font-size: 16px;
  }
  .employee-email {
    position: absolute;
    left: 0; right: 0;
    top: 234px;
    font-size: 16px;
  }
  .company-web {
    position: absolute;
    left: 0; right: 0;
    top: 439px;
    font-size: 16px;
  }
</style>
</head>
<body>
<main class="canvas">
  <section class="card card-front orange-surface" role="img" aria-label="Orange textured card front with Brivalo name">
    <div class="front-wordmark">
      <span class="mark-square"></span>
      <span class="brand-name">BRIVALO</span>
    </div>
  </section>

  <section class="card card-back">
    <div class="back-color-panel orange-surface" role="img" aria-label="Orange textured paper surface"></div>
    <div class="back-info-panel">
      <div class="back-wordmark">
        <span class="mark-square"></span>
        <span class="brand-name">BRIVALO</span>
      </div>
      <div class="employee-name">DANIEL HARPER</div>
      <div class="employee-phone">0400 732 918</div>
      <div class="employee-email">d.harper@brivalo.com</div>
      <div class="company-web">www.brivalo.com</div>
    </div>
  </section>
</main>
</body>
</html>
```